Kiosk Coin Venture: Safe and Secure Cash Money

Front of card: LOGO

Back of card:
$$$ FREE ATM PLACEMENT $$$
BENIFITS OF HAVING AN ATM AT YOUR BUSINESS
FREE ATM and BTM (Bitcoin) installation, maintenance, and loading.
Lower card processing fees
Stimulate more traffic.
Ease of access for customers
Maintain customers inside location.
Higher tips and spending

Contact me for more information!
Name: Tobias Merlano
Phone: (512) 638-9071 - Call or Text
Email: Tobias@KioskCoin.example

Contact Information for Business Card

The card should be shape of the logo. Only the back will have all the contact and business details.

Requirements
Must have
• The logo itself will be one side, the card will be the shape of the logo. contact details on back side.

```html
<!DOCTYPE html>
<html lang="en">
<head>
<meta charset="utf-8">
<title>Kiosk Coin Venture – Business Card</title>
<link rel="stylesheet" href="https://fonts.googleapis.com/css2?family=Jost:wght@300;400;600;700&display=swap">
<style>
  :root {
    --page: #ffffff;
    --card: #050505;
    --card-edge: #1c1c1c;
    --silver: #a8a8a8;
    --silver-light: #c9c9c9;
    --silver-dark: #8e8e8e;
  }
  * { margin: 0; padding: 0; box-sizing: border-box; }
  html, body {
    width: 1200px; height: 846px; overflow: hidden;
    background: var(--page);
    font-family: "Jost", sans-serif;
  }
  .canvas { position: relative; width: 1200px; height: 846px; }

  .card { position: absolute; }
  .card svg { position: absolute; inset: 0; display: block; }
  .card-front { left: 262px; top: 203px; width: 292px; height: 446px; }
  .card-back  { left: 658px; top: 201px; width: 294px; height: 453px; }

  .front-brand {
    position: absolute; left: 0; right: 0; top: 150px;
    display: flex; flex-direction: column; align-items: center; gap: 18px;
  }
  .brand-dot {
    width: 64px; height: 64px; border-radius: 50%;
    background: var(--silver);
  }
  .brand-name {
    color: var(--silver-light);
    font-weight: 600; font-size: 30px; line-height: 1.1;
    text-align: center; letter-spacing: 0.04em; text-transform: uppercase;
    width: 220px;
  }

  .back-content {
    position: absolute; inset: 0;
    color: var(--silver);
    text-align: center;
  }
  .offer-title {
    position: absolute; left: 0; right: 0; top: 66px;
    font-weight: 700; font-size: 18px; letter-spacing: 0.01em;
  }
  .offer-sub {
    position: absolute; left: 0; right: 0; top: 87px;
    font-weight: 300; font-size: 11.5px; letter-spacing: 0.01em;
  }
  .offer-service {
    position: absolute; left: 0; right: 0; top: 110px;
    font-weight: 600; font-size: 12.5px; line-height: 16.5px;
  }
  .benefits {
    position: absolute; left: 29px; top: 163px;
    list-style: none; text-align: left;
    font-weight: 300; font-size: 15.5px; letter-spacing: 0.06em; line-height: 20px;
  }
  .benefits li { position: relative; padding-left: 12px; margin-bottom: 4.5px; }
  .benefits li::before {
    content: ""; position: absolute; left: 1px; top: 7px;
    width: 6px; height: 6px; background: var(--silver);
    transform: rotate(45deg) scaleY(1.3);
  }
  .contact-name {
    position: absolute; left: 0; right: 0; top: 320px;
    font-weight: 600; font-size: 19px; color: var(--silver-dark);
  }
  .contact-line {
    position: absolute; left: 0; right: 0;
    font-weight: 600; font-size: 13px;
  }
  .contact-phone { top: 351px; }
  .contact-email { top: 372px; }
</style>
</head>
<body>
<main class="canvas">

  <section class="card card-front" aria-label="Card front">
    <svg viewBox="0 0 292 446" width="292" height="446">
      <defs>
        <linearGradient id="edge-metal" x1="0" y1="0" x2="1" y2="0">
          <stop offset="0" stop-color="#d8d8d8"/>
          <stop offset="0.5" stop-color="#8a8a8a"/>
          <stop offset="1" stop-color="#d8d8d8"/>
        </linearGradient>
      </defs>
      <path d="M146 1 L291 46 V322 C291 385 200 418 146 445 C92 418 1 385 1 322 V46 Z"
            fill="url(#edge-metal)"/>
      <path d="M146 6 L286 49 V321 C286 380 198 413 146 439 C94 413 6 380 6 321 V49 Z"
            fill="var(--card-edge)"/>
    </svg>
    <div class="front-brand">
      <span class="brand-dot"></span>
      <span class="brand-name">Kiosk Coin Venture</span>
    </div>
  </section>

  <section class="card card-back" aria-label="Card back">
    <svg viewBox="0 0 294 453" width="294" height="453">
      <path d="M147 0 L294 46 V328 C294 390 200 425 147 453 C94 425 0 390 0 328 V46 Z"
            fill="var(--card)"/>
    </svg>
    <div class="back-content">
      <h1 class="offer-title">$$$ FREE ATM PLACEMENT $$$</h1>
      <p class="offer-sub">BENIFITS OF HAVING AN ATM AT YOUR BUSINESS</p>
      <p class="offer-service">FREE ATM and BTM (Bitcoin)<br>installation / maintenance / loading</p>
      <ul class="benefits">
        <li>Lower card processing fees</li>
        <li>Stimulate more traffic</li>
        <li>Ease of access for customers</li>
        <li>Maintain customers inside<br>location</li>
        <li>Higher tips and spending</li>
      </ul>
      <p class="contact-name">Tobias Merlano</p>
      <p class="contact-line contact-phone">(512) 638-9071 - Call or Text</p>
      <p class="contact-line contact-email">Tobias@KioskCoin.example</p>
    </div>
  </section>

</main>
</body>
</html>
```